K.O.V Ventures - Business Card

We need a business card design for a new company based in Malaysia, called K.O.V Ventures Sdn. Bhd. We create, develop & customize database & software/web-based business systems to suit our clients need, mainly in oil&gas industry.

We would like to challenge the creativity of you to design a simple, meaningful, modern, professional & sleek. The design concept may varies but worthy enough for the recipients to proudly keep it in their wallet, and award us with fruitful business opportunities.

B-7-12 Lantera Plaza,
PJU9/4, Damai Perdana,
47500 Selangor. Malaysia

http://kovventures-example.com

HAFIZ Rosman | +6012-7038812 | Co-Founder
Di Kamarul | +6012-4190273 | Co-Founder
Amir Syukri | +6019-3306158 | Managing Director

Target Market(s)

The target market will expand to several other industries such as aviation, communication, automotive, education & hotel.

Industry/Entity Type

Business

Font styles to use
Serif
Sans Serif
Decorative
Script

Requirements
Must have
• plain background yet colourful concept.
Should not have
• something too easy that I can draw myself

```html
<!DOCTYPE html>
<html lang="en">
<head>
<meta charset="utf-8">
<title>K.O.V Ventures - Business Card</title>
<link rel="stylesheet" href="https://fonts.googleapis.com/css2?family=Arimo:wght@400;700&display=swap">
<style>
  :root {
    --page: #e8e4de;
    --card-light: #6b6b6b;
    --card-dark: #2c2c2c;
    --ink-white: #ffffff;
    --accent: #e6dc00;
    --ink-black: #111111;
    --font: "Arimo", Arial, sans-serif;
  }
  * { box-sizing: border-box; margin: 0; padding: 0; }
  html, body { width: 1200px; height: 900px; overflow: hidden; background: var(--page); }
  .canvas { position: relative; width: 1200px; height: 900px; }
  .card {
    position: absolute; left: 350px; top: 40px; width: 500px; height: 820px;
    border-radius: 70px 10px 70px 10px;
    background: radial-gradient(ellipse 75% 55% at 50% 30%, var(--card-light), var(--card-dark) 100%);
    overflow: hidden; font-family: var(--font); color: var(--ink-white);
    box-shadow: 0 6px 18px rgba(0,0,0,.25);
  }
  .brand { position: absolute; top: 95px; left: 0; right: 0; display: flex; justify-content: center; align-items: center; gap: 14px; }
  .brand-square { width: 46px; height: 46px; background: var(--accent); }
  .brand-name { font-size: 36px; font-weight: 700; color: var(--ink-white); }
  .founders { position: absolute; top: 232px; left: 80px; font-size: 24px; line-height: 28px; }
  .founder { position: relative; white-space: nowrap; }
  .founder .phone { position: absolute; left: 176px; }
  .role { color: var(--accent); font-size: 19px; }
  .founders .role { display: block; text-align: center; width: 330px; margin-top: 4px; }
  .director { position: absolute; top: 342px; left: 0; right: 0; text-align: center; }
  .director-name { font-size: 36px; }
  .director .role { display: block; margin-top: 6px; }
  .contact { position: absolute; left: 95px; display: flex; align-items: flex-start; gap: 24px; font-size: 24px; line-height: 28px; white-space: nowrap; }
  .contact svg { flex: none; }
  .icon-solid { fill: var(--ink-white); }
  .icon-line { fill: none; stroke: var(--ink-white); stroke-width: 2.5; }
  .contact-phone { top: 440px; align-items: center; }
  .contact-address { top: 510px; }
  .contact-web { top: 612px; left: 95px; align-items: center; font-size: 21px; gap: 18px; }
  .tagline-band { position: absolute; top: 672px; left: 0; right: 0; height: 62px; background: var(--accent);
    color: var(--ink-black); font-size: 48px; letter-spacing: 7px; text-align: center; line-height: 64px; }
  .tagline-end { position: absolute; top: 742px; left: 0; right: 0; text-align: center;
    font-size: 46px; font-weight: 700; letter-spacing: 22px; padding-left: 22px; }
</style>
</head>
<body>
<main class="canvas">
  <section class="card" aria-label="K.O.V Ventures business card">
    <div class="brand">
      <span class="brand-square"></span>
      <span class="brand-name">K.O.V Ventures</span>
    </div>

    <div class="founders">
      <div class="founder">HAFIZ Rosman - +6012-7038812</div>
      <div class="founder">Di Kamarul - <span class="phone">+6012-4190273</span></div>
      <span class="role">Co-Founder</span>
    </div>

    <div class="director">
      <div class="director-name">Amir Syukri</div>
      <span class="role">Managing Director</span>
    </div>

    <div class="contact contact-phone">
      <svg class="icon-solid" width="30" height="46" viewBox="0 0 30 46" aria-hidden="true">
        <path d="M10 2c3 0 5 1 5 3l1 9c0 2-3 3-5 4 0 4 1 8 3 11 2-1 4-2 6-1l5 7c1 2 0 4-3 6-3 2-7 2-9-1C7 33 4 24 4 14 4 7 6 2 10 2z"/>
      </svg>
      <span>+6019-3306158</span>
    </div>

    <div class="contact contact-address">
      <svg class="icon-solid" width="36" height="34" viewBox="0 0 36 34" aria-hidden="true">
        <path d="M18 2 2 16h5v16h9V22h4v10h9V16h5L28 7V3h-4v1z"/>
      </svg>
      <span>B-7-12 Lantera Plaza,<br>PJU9/4, Damai Perdana,<br>47500 Selangor, Malaysia</span>
    </div>

    <div class="contact contact-web">
      <svg class="icon-line" width="40" height="40" viewBox="0 0 40 40" aria-hidden="true">
        <circle cx="20" cy="20" r="17"/>
        <ellipse cx="20" cy="20" rx="7" ry="17"/>
        <line x1="3" y1="20" x2="37" y2="20"/>
        <path d="M6 11h28M6 29h28"/>
      </svg>
      <span>http://kovventures-example.com</span>
    </div>

    <div class="tagline-band">WE REACH</div>
    <div class="tagline-end">WIDE</div>
  </section>
</main>
</body>
</html>
```